Commercial Security Landing Page

We're looking for a simple customizable Bootstrap based single landing page similar to http://velmorkit.example/preview/QX482T901

I have attached our Full Logo to incorporate into the design.
I can also attach other assets if required.

We're in the Commercial Security Industry, we specialize in (These must be included on the site):
- CCTV
- Access Control
- Automation
- Fire Monitoring
- Theft Protection/Burglar Alarms

More information:
We install these systems in customers businesses to protect them from theft, fire, etc. We do very high quality installs and only use the highest quality equipment for each customer. We do not do network security or anything like that, we focus completely in protecting businesses and homes through the use of CCTV, Access Control, Automation such as (light control, garage control, flood protection, etc), we also handle fire monitoring, theft protection, and burglar alarms.

Specs/Requirements:
- Must not be built with WordPress.
- Must be built using Twitter Bootstrap
- Any images used must not be copyright protected or contain royalties.
- Eye Catching Stock Photos or Placeholder so that we can replace with our own photos.
- SEO Friendly
- Easily adjustable
- Contains a contact form
- Customized to our industry.
- Must be "modern" and scalable across all devices.

Colors we like:
- #0C9ED9
- #595A5C
- #414142

Target Market(s)

Business Owners, Home Owners, Enterprise

Industry/Entity Type

Security Service

Coding

Coded - Design and coding required

Font styles to use
Sans Serif

Requirements
Must have
• Must contain highlights of the following bullet points:
• - CCTV
• - Access Control
• - Automation
• - Fire Monitoring
• - Theft Protection/Burglar Alarms
Nice to have
• - Twitter Bootstrap
• - Any images used must not be copyright protected or contain royalties.
• - Eye Catching Stock Photos or Placeholder so that we can replace with our own photos.
• - SEO Friendly
• Partner Section (Showing off our partners):
• Brivanta.net (https://www.brivanta.example/)
• Kelsomir Gate (http://www.kelsomirgate.example/)
• TRV (http://www.torvanblazecare.example/)
Should not have
• Should not be built on Wordpress

```html
<!DOCTYPE html>
<html lang="en">
<head>
<meta charset="utf-8">
<title>Norvex — Commercial Security</title>
<link rel="stylesheet" href="https://fonts.googleapis.com/css2?family=Montserrat:wght@500;600;700&family=Poppins:wght@300;400;500;600&display=swap">
<style>
:root{
  --blue:#0C9ED9;
  --grey:#595A5C;
  --dark:#414142;
  --ink:#2b2b2c;
  --footer:#232323;
  --light:#f3f4f5;
  --line:#dfe3e6;
  --white:#ffffff;
}
*{box-sizing:border-box;margin:0;padding:0}
html,body{width:1200px;height:2961px;overflow:hidden}
body{font-family:"Poppins",sans-serif;color:var(--grey);background:var(--white);position:relative}
section,header,footer{position:relative;width:1200px}
.brand{font-family:"Poppins",sans-serif;font-weight:600;color:var(--blue);display:flex;align-items:center;gap:10px}
.brand .brand-mark{width:26px;height:26px;background:var(--blue);border-radius:4px}

/* header */
.site-header{height:69px;display:flex;align-items:center}
.site-header .brand{position:absolute;left:112px;top:14px;font-size:34px;line-height:40px}
.main-nav{position:absolute;left:549px;top:20px;display:flex}
.main-nav a{font-size:13px;color:var(--grey);text-decoration:none;line-height:29px;height:31px;text-align:center}
.main-nav a.active{border:1.5px solid var(--blue);border-radius:3px;color:var(--blue);width:79px;margin-right:30px}
.main-nav a:nth-child(2){width:80px}
.main-nav a:nth-child(3){width:150px}
.main-nav a:nth-child(4){width:70px}
.main-nav a:nth-child(5){width:150px}

/* hero */
.hero{height:602px;overflow:hidden}
.hero-photo{position:absolute;inset:0;background:
  radial-gradient(ellipse 380px 330px at 860px 280px,#a8aaad 0%,#5d6064 45%,transparent 75%),
  radial-gradient(circle 70px at 820px 320px,#6a1d1d 0%,#2a2b2e 70%,transparent 100%),
  linear-gradient(100deg,#3d4147 0%,#5c6167 40%,#7a7e83 70%,#4a4d52 100%)}
.hero-card{position:absolute;left:118px;top:187px;width:425px;height:330px;border:7px solid var(--blue);border-radius:46px 10px 46px 10px;background:rgba(40,44,50,.82);padding:0}
.hero-card::after{content:"";position:absolute;inset:8px -16px -16px 8px;border:3px solid var(--blue);border-radius:46px 10px 46px 10px;pointer-events:none}
.hero-card h1{position:absolute;left:44px;top:70px;font-weight:300;font-size:58px;line-height:62px;color:var(--white);letter-spacing:.5px}
.hero-card p{position:absolute;left:44px;top:208px;font-size:28px;font-weight:300;color:var(--blue);letter-spacing:.5px}

/* welcome */
.welcome{height:356px;text-align:center}
.section-title{display:flex;justify-content:center;align-items:center;gap:10px;font-family:"Montserrat",sans-serif;font-weight:600;font-size:26px;color:var(--ink);padding-top:80px}
.section-title .brand{font-size:30px}
.title-rule{position:relative;width:510px;height:1px;background:var(--line);margin:10px auto 0}
.title-rule::after{content:"";position:absolute;left:50%;top:0;margin-left:-6px;border:6px solid transparent;border-top-color:var(--dark)}
.welcome-copy{width:940px;margin:24px auto 0;font-size:12px;line-height:22.5px;color:var(--grey)}
.btn-outline{display:inline-block;margin-top:34px;width:78px;height:31px;line-height:28px;border:1.5px solid var(--blue);border-radius:4px;color:var(--blue);font-size:11px;font-weight:600;text-decoration:none;letter-spacing:.5px}

/* services diagram */
.services{height:592px}
.service{position:absolute;text-align:center}
.service h3{font-family:"Montserrat",sans-serif;font-weight:600;font-size:17px;color:var(--blue);letter-spacing:.3px;margin-bottom:14px;white-space:nowrap}
.frame{position:relative;width:190px;height:150px;border:6px solid var(--blue);border-radius:32px 8px 32px 8px;overflow:visible}
.frame::after{content:"";position:absolute;inset:4px -12px -12px 4px;border:2.5px solid var(--blue);border-radius:32px 8px 32px 8px}
.frame .photo{position:absolute;inset:6px;border-radius:24px 4px 24px 4px}
.photo-access{background:linear-gradient(135deg,#2c3036,#8a8f96 60%,#d8c2a8)}
.photo-fire{background:linear-gradient(135deg,#f2efe9,#c9c3b8 55%,#b3322c 80%,#e9e4dd)}
.photo-auto{background:linear-gradient(135deg,#dfe5ea,#43506b 50%,#f3f3f3)}
.photo-cctv{background:linear-gradient(160deg,#f1f1f1,#c9c9c9 45%,#c0402f 75%,#ececec)}
.photo-theft{background:linear-gradient(135deg,#1e1f22,#6a6c70 50%,#b28a4a 70%,#2a2b2e)}
.svc-access{left:170px;top:66px;width:201px}
.svc-fire{left:500px;top:12px;width:200px}
.svc-auto{left:821px;top:66px;width:203px}
.svc-cctv{left:114px;top:320px;width:202px}
.svc-theft{left:880px;top:320px;width:206px}
.hub{position:absolute;left:480px;top:331px;width:230px;height:177px;border:8px solid var(--blue);border-radius:40px 10px 40px 10px;display:flex;align-items:center;justify-content:center}
.hub::after{content:"";position:absolute;inset:6px -16px -16px 6px;border:3px solid var(--blue);border-radius:40px 10px 40px 10px}
.hub .brand{font-size:40px}
.arrows{position:absolute;left:0;top:0;width:1200px;height:592px}

/* testimonials */
.testimonials{height:434px;background:var(--blue);color:var(--white);text-align:center}
.testimonials .section-title{color:var(--white);padding-top:56px}
.testimonials .title-rule{background:rgba(255,255,255,.45)}
.testimonials .title-rule::after{border-top-color:var(--white)}
.people{position:absolute;top:152px;left:0;width:1200px}
.person{position:absolute;width:200px;text-align:center}
.avatar{width:68px;height:68px;border-radius:50%;margin:0 auto;background:linear-gradient(180deg,#ffffff,#dcdfe2);border:2px solid var(--white)}
.avatar.featured{background:linear-gradient(160deg,#d8a27a,#8a5a3c 60%,#2f4c6e)}
.person span{display:block;margin-top:10px;font-size:11.5px;font-weight:500}
.person.current span::after{content:"";display:block;width:0;height:0;margin:5px auto 0;border:5px solid transparent;border-top-color:var(--white)}
.quote{position:absolute;left:180px;top:266px;width:840px;height:109px;background:var(--light);border-radius:3px;box-shadow:0 2px 4px rgba(0,0,0,.18);color:var(--dark);font-size:12.5px;font-style:italic;line-height:25px;padding:12px 46px 0}
.quote::before,.quote::after{position:absolute;font-size:34px;color:#c6cacd;font-style:normal;font-family:Georgia,serif}
.quote::before{content:"\201C";left:38px;top:6px}
.quote::after{content:"\201D";right:98px;bottom:-8px}

/* contact */
.contact{height:488px;text-align:center}
.contact .section-title{padding-top:46px}
.contact .title-rule{width:260px;margin-top:16px}
.contact .title-rule::after{border-top-color:var(--blue)}
.contact-form{position:absolute;left:249px;top:160px;width:701px}
.field{position:absolute;height:38px;background:linear-gradient(180deg,#ffffff,#eef0f2);border:1px solid var(--line);border-radius:2px;font-size:12px;color:var(--dark);text-align:left;padding:10px 12px;font-family:"Poppins",sans-serif}
.f-name{left:0;top:0;width:341px}
.f-email{left:359px;top:0;width:342px}
.f-phone{left:0;top:55px;width:341px}
.f-subject{left:359px;top:55px;width:342px}
.f-message{left:0;top:110px;width:701px;height:97px}
.btn-solid{position:absolute;left:300px;top:245px;width:102px;height:30px;border-radius:4px;background:var(--blue);color:var(--white);font-size:11px;font-weight:600;line-height:30px;letter-spacing:.5px;border:0}

/* footer */
.site-footer{height:420px;background:var(--footer);color:#e6e6e6}
.partners{position:absolute;left:112px;top:0;width:976px;height:104px}
.partners svg{position:absolute;inset:0}
.partner-row{position:absolute;inset:0 0 14px;display:flex;align-items:center;justify-content:center;gap:90px}
.partner{font-family:"Poppins",sans-serif;font-weight:600;font-size:22px;color:var(--dark);display:flex;align-items:center;gap:8px}
.partner .dot{width:22px;height:22px;background:#f2a33a;border-radius:3px}
.partner .ring{width:24px;height:24px;border-radius:50%;background:var(--dark)}
.badge{width:76px;height:76px;border-radius:50%;background:linear-gradient(180deg,#c33c2a,#7a1f17)}
.footer-brand{position:absolute;left:112px;top:223px;font-size:44px}
.footer-col{position:absolute;top:175px}
.footer-col h4{font-family:"Montserrat",sans-serif;font-weight:600;font-size:15px;color:var(--white);letter-spacing:.4px;margin-bottom:16px}
.quick-links{left:547px}
.quick-links li{list-style:none;font-size:11px;line-height:28px;color:#dcdcdc}
.quick-links li::before{content:"›";margin-right:9px;color:#cfcfcf}
.contact-info{left:809px;width:290px}
.info-row{display:flex;gap:12px;font-size:11px;line-height:16px;margin-bottom:12px}
.info-row svg{flex:0 0 14px;margin-top:1px}
.info-row strong{display:block;font-weight:500;font-size:12px;color:var(--white)}
.info-row.phone{font-size:14px;font-weight:600;color:var(--white)}
.copyright{position:absolute;left:112px;top:365px;width:976px;border-top:1px solid #3a3a3a;text-align:center;font-size:11px;padding-top:17px;color:#d8d8d8}
</style>
</head>
<body>

<header class="site-header">
  <div class="brand"><span class="brand-mark"></span>Norvex</div>
  <nav class="main-nav">
    <a class="active" href="#home">Home</a>
    <a href="#about">About</a>
    <a href="#services">Services</a>
    <a href="#blog">Blog</a>
    <a href="#contact">Contact</a>
  </nav>
</header>

<section class="hero" id="home">
  <div class="hero-photo" role="img" aria-label="Close-up of a commercial CCTV security camera with red infrared lights"></div>
  <div class="hero-card">
    <h1>Professional<br>&amp; Powerful</h1>
    <p>SECURITY PROTECTION</p>
  </div>
</section>

<section class="welcome" id="about">
  <h2 class="section-title">WELCOME TO <span class="brand">Norvex</span></h2>
  <div class="title-rule"></div>
  <p class="welcome-copy">Welcome enim ad minim veniam, quis nostrud exercitation ullamco laboris nisi ut aliquip ex ea commodo consequat. Duis aute irure dolor in reprehenderit in voluptate velit esse cillum dolore eu fugiat nulla pariatur. Excepteur sint occaecat cupidatat non proident, sunt Duis aute irure dolor in reprehenderit in voluptate velit esse cillum dolore eu fugiat nulla pariatur in culpa qui officia deserunt mollitanim id . Duis aute irure dolor in reprehenderit in voluptate velit esse cillum dolore eu fugiat nulla pariatur in culpa qui officia deserunt mollitanim id est laborum.</p>
  <a class="btn-outline" href="#services">MORE</a>
</section>

<section class="services" id="services">
  <svg class="arrows" viewBox="0 0 1200 592" aria-hidden="true">
    <defs>
      <marker id="head" viewBox="0 0 10 10" refX="8" refY="5" markerWidth="9" markerHeight="9" orient="auto">
        <path d="M1 1 L8 5 L1 9" fill="none" stroke="#0C9ED9" stroke-width="1.4"/>
      </marker>
    </defs>
    <g stroke="#0C9ED9" stroke-width="2.2" fill="none" marker-end="url(#head)">
      <line x1="608" y1="310" x2="608" y2="220"/>
      <line x1="470" y1="338" x2="383" y2="276"/>
      <line x1="730" y1="334" x2="825" y2="268"/>
      <line x1="462" y1="440" x2="336" y2="440"/>
      <line x1="734" y1="440" x2="864" y2="440"/>
    </g>
  </svg>

  <div class="service svc-fire"><h3>FIRE MONITORING</h3><div class="frame"><div class="photo photo-fire" role="img" aria-label="Red fire alarm device mounted on a wall"></div></div></div>
  <div class="service svc-access"><h3>ACCESS CONTROL</h3><div class="frame"><div class="photo photo-access" role="img" aria-label="Hand holding an access card to a door reader"></div></div></div>
  <div class="service svc-auto"><h3>AUTOMATION</h3><div class="frame"><div class="photo photo-auto" role="img" aria-label="Security staff at a building control desk"></div></div></div>
  <div class="service svc-cctv"><h3>CCTV</h3><div class="frame"><div class="photo photo-cctv" role="img" aria-label="CCTV camera watching over an office interior"></div></div></div>
  <div class="service svc-theft"><h3>THEFT PROTECTION</h3><div class="frame"><div class="photo photo-theft" role="img" aria-label="Laptop secured with a chain and padlock"></div></div></div>

  <div class="hub"><div class="brand">Norvex</div></div>
</section>

<section class="testimonials">
  <h2 class="section-title">TESTIMONIALS</h2>
  <div class="title-rule"></div>
  <div class="people">
    <div class="person" style="left:206px"><div class="avatar" role="img" aria-label="Client portrait placeholder"></div><span>Mr. Dorin Vale</span></div>
    <div class="person current" style="left:500px"><div class="avatar featured" role="img" aria-label="Client portrait photo"></div><span>Mr. Kasim Orlo</span></div>
    <div class="person" style="left:790px"><div class="avatar" role="img" aria-label="Client portrait placeholder"></div><span>Ms. Lenna Brisk</span></div>
  </div>
  <blockquote class="quote">Lorem ipsum dolor sit amet, consectetuer adipiscing elit, sed diam nonummy nibh euismod tincidunt ut laoreet dolore magna aliquam erat volutpat. Ut wisi enim ad minim veniam, quis nostrud exerci tation ullamcorper suscipit lobortis nisl ut aliquip ex ea commodo consequat. Duis autem vel eum &nbsp;dignissim qui blandit praesent luptatum zzril delenit augue.</blockquote>
</section>

<section class="contact" id="contact">
  <h2 class="section-title">CONTACT US</h2>
  <div class="title-rule"></div>
  <form class="contact-form">
    <div class="field f-name">Name:</div>
    <div class="field f-email">Email:</div>
    <div class="field f-phone">Phone No:</div>
    <div class="field f-subject">Subject:</div>
    <div class="field f-message">Phone No:</div>
    <button class="btn-solid" type="button">SUBMIT</button>
  </form>
</section>

<footer class="site-footer">
  <div class="partners">
    <svg viewBox="0 0 976 104" preserveAspectRatio="none" aria-hidden="true">
      <path d="M0 0 H976 V72 Q976 86 958 88 Q488 112 18 88 Q0 86 0 72 Z" fill="#f4f4f5"/>
    </svg>
    <div class="partner-row">
      <div class="partner"><span class="dot"></span>Kelsomir Gate</div>
      <div class="partner"><span class="ring"></span>Brivanta.net</div>
      <div class="badge" role="img" aria-label="TRV partner badge"></div>
    </div>
  </div>

  <div class="brand footer-brand"><span class="brand-mark"></span>Norvex</div>

  <div class="footer-col quick-links">
    <h4>QUICK LINKS</h4>
    <ul>
      <li>Home</li><li>About Norvex</li><li>Our Services</li><li>Our Blog</li><li>Contact Us</li>
    </ul>
  </div>

  <div class="footer-col contact-info">
    <h4>CONTACT INFO</h4>
    <div class="info-row">
      <svg width="14" height="16" viewBox="0 0 14 16"><path d="M7 0C3.7 0 1.2 2.5 1.2 5.6 1.2 9.6 7 16 7 16s5.8-6.4 5.8-10.4C12.8 2.5 10.3 0 7 0zm0 8a2.4 2.4 0 1 1 0-4.8A2.4 2.4 0 0 1 7 8z" fill="#fff"/></svg>
      <div><strong>Main Office</strong>Norvex Security Solutions dolar lorem ipsum Ut wisi enim ad minim.</div>
    </div>
    <div class="info-row phone">
      <svg width="14" height="14" viewBox="0 0 14 14"><path d="M3 .5l2 2.6-1.2 1.8c.8 1.8 2.3 3.3 4.1 4.1l1.8-1.2L12.3 9.8 11 12.6C5.6 12.9 1.1 8.4 1.4 3z" fill="#fff"/></svg>
      <div>555-014-2290</div>
    </div>
    <div class="info-row">
      <svg width="14" height="11" viewBox="0 0 14 11"><rect x="0" y="0" width="14" height="11" rx="1.5" fill="#fff"/><path d="M1 1.5l6 4.5 6-4.5" stroke="#232323" stroke-width="1.3" fill="none"/></svg>
      <div>info@norvex.example</div>
    </div>
  </div>

  <div class="copyright">All rights Reserved 2017</div>
</footer>

</body>
</html>
```